Banner Design for Cryptocurrencie Exchange

We need for our new Homepage, very modern and stylish Banners:

Our new Homepage:
www.marvoly.com

Example what looks nice:
https://www.pelnor-blick.de/wp-content/uploads/2017/01/lunatrakhost_sidebar.gif

We want GIF Animated Banners, but we are also open for a fixed Banner if we can combine every Information on it.

Informations on the Banner:

- Cryptocurrencies
- Exchange
- Multi Crypto
- Multi Fiat
- KRV / ZLT / NOX / VELCON / DRAM / etc...
- EURO / USD / TLY / CHF / etc...
- Payment Options (Vorn / Glimra / Trovan / Zelbix / CREDITCARD)
- Easy to Use
- All in One Plattform (Exchange, Mining, ATMs, Payment Solution)

If you need any further Information feel free to contact us.

Thank you :)

```html
<!DOCTYPE html>
<html lang="en">
<head>
<meta charset="utf-8">
<title>Marvoly – Banner Frames</title>
<link rel="stylesheet" href="https://fonts.googleapis.com/css2?family=Barlow:wght@500;600;700&display=swap">
<style>
  :root {
    --stage-light: #eef2ec;
    --stage-mid: #dfe5e4;
    --stage-dark: #c9cfd6;
    --navy: #0f2746;
    --navy-deep: #0a1c35;
    --ink: #161616;
    --white: #ffffff;
    --brand-blue: #1f5fb0;
    --red: #e8505b;
    --orange: #f29a1d;
    --green: #2db37a;
    --sky: #2aa6df;
    --yellow: #f4c21b;
    --lime: #3fbf4a;
    --hex-blue: #1e78d6;
    --hex-green: #34b04f;
    --hex-purple: #8a2fa8;
    --hex-red: #e2463b;
  }
  * { margin: 0; padding: 0; box-sizing: border-box; }
  html, body { width: 1200px; height: 218px; overflow: hidden; }
  body {
    position: relative;
    font-family: "Barlow", Arial, sans-serif;
    background: linear-gradient(90deg, var(--stage-light) 0%, var(--stage-mid) 45%, var(--stage-dark) 100%);
  }
  .frame {
    position: absolute;
    top: 28px;
    width: 159px;
    height: 133px;
    overflow: hidden;
    color: var(--white);
    background: linear-gradient(160deg, #163458 0%, var(--navy) 55%, var(--navy-deep) 100%);
  }
  .frame-label {
    position: absolute;
    top: 176px;
    width: 159px;
    text-align: center;
    font-weight: 700;
    font-size: 11px;
    letter-spacing: 0.08em;
    color: var(--ink);
  }
  .f1 { left: 49px; } .f2 { left: 249px; } .f3 { left: 448px; }
  .f4 { left: 629px; } .f5 { left: 812px; } .f6 { left: 1001px; }
  .abs { position: absolute; }
  .center-x { left: 0; width: 100%; text-align: center; }

  /* Frame 1 */
  .city-scene {
    position: absolute; inset: 0;
    background: linear-gradient(180deg, #f6f7f8 0%, #d9dde2 35%, #8d8a8e 65%, #3b3a4a 100%);
  }
  .brand {
    position: absolute; top: 14px; left: 0; width: 100%;
    display: flex; justify-content: center; align-items: center; gap: 5px;
  }
  .brand-mark { width: 16px; height: 16px; background: var(--brand-blue); }
  .brand-name { font-weight: 600; font-size: 14px; color: var(--brand-blue); letter-spacing: 0.04em; }
  .brand-tagline {
    position: absolute; top: 32px; left: 60px;
    font-size: 4.5px; font-weight: 600; color: #333; letter-spacing: 0.05em;
  }

  /* Frame 2 */
  .circuit-scene {
    position: absolute; inset: 0;
    background: radial-gradient(circle at 52% 63%, #8a6a24 0 18%, #2a2a33 30%, #121219 70%);
  }
  .frame-title {
    font-weight: 700; font-size: 12px; letter-spacing: 0.06em;
  }

  /* Frame 3 / 4 / 6 text */
  .feature { font-weight: 600; font-size: 10px; letter-spacing: 0.04em; }
  .codes { font-weight: 700; font-size: 9px; letter-spacing: 0.06em; line-height: 12.5px; }
  .icon { position: absolute; }

  /* Frame 5 */
  .pay-title { font-weight: 700; font-size: 11.5px; letter-spacing: 0.05em; }
  .pay-box {
    position: absolute; height: 19px; width: 49px;
    background: var(--white); color: var(--navy);
    font-weight: 700; font-size: 9px;
    display: flex; align-items: center; justify-content: center;
  }
  .pay-card { width: 32px; height: 20px; font-size: 7.5px; }

  .hub-label { font-weight: 600; font-size: 7.5px; letter-spacing: 0.03em; }
</style>
</head>
<body>

  <!-- Frame 1 -->
  <section class="frame f1">
    <div class="city-scene" role="img" aria-label="Businessman walking up a bright staircase toward the sky above a night city"></div>
    <div class="brand"><span class="brand-mark"></span><span class="brand-name">MARVOLY</span></div>
    <div class="brand-tagline">THE FUTURE OF MONEY</div>
  </section>
  <div class="frame-label f1">FRAME 1</div>

  <!-- Frame 2 -->
  <section class="frame f2">
    <div class="circuit-scene" role="img" aria-label="Golden coin in the centre of a glowing circuit board"></div>
    <div class="abs center-x frame-title" style="top:16px">CRYPTOCURRENCIES</div>
  </section>
  <div class="frame-label f2">FRAME 2</div>

  <!-- Frame 3 -->
  <section class="frame f3">
    <svg class="icon" style="left:30px;top:20px" width="22" height="22" viewBox="0 0 22 22" aria-hidden="true">
      <circle cx="11" cy="11" r="7" fill="none" stroke="var(--red)" stroke-width="2"/>
      <path d="M3 6 L3 2 M3 6 L7 6 M19 16 L19 20 M19 16 L15 16" stroke="var(--red)" stroke-width="2" stroke-linecap="round"/>
      <text x="11" y="14.5" font-size="9" font-weight="700" text-anchor="middle" fill="var(--red)">$</text>
    </svg>
    <svg class="icon" style="left:104px;top:20px" width="22" height="22" viewBox="0 0 22 22" aria-hidden="true">
      <circle cx="11" cy="11" r="9" fill="none" stroke="var(--orange)" stroke-width="2"/>
      <circle cx="11" cy="11" r="4" fill="none" stroke="var(--orange)" stroke-width="2"/>
    </svg>
    <div class="abs feature" style="left:0;width:82px;text-align:center;top:45px">Exchange</div>
    <div class="abs feature" style="left:74px;width:82px;text-align:center;top:45px">Multi Crypto</div>
    <svg class="icon" style="left:30px;top:73px" width="22" height="22" viewBox="0 0 22 22" aria-hidden="true">
      <circle cx="11" cy="11" r="9" fill="none" stroke="var(--green)" stroke-width="2"/>
      <text x="11" y="15" font-size="11" font-weight="700" text-anchor="middle" fill="var(--green)">€</text>
    </svg>
    <svg class="icon" style="left:104px;top:73px" width="22" height="22" viewBox="0 0 22 22" aria-hidden="true">
      <circle cx="11" cy="11" r="9" fill="none" stroke="var(--sky)" stroke-width="2"/>
      <path d="M7 11 L10 14 L15 8" fill="none" stroke="var(--sky)" stroke-width="2" stroke-linecap="round"/>
    </svg>
    <div class="abs feature" style="left:0;width:82px;text-align:center;top:103px">Multi Fiat</div>
    <div class="abs feature" style="left:74px;width:82px;text-align:center;top:103px">Easy to use</div>
  </section>
  <div class="frame-label f3">FRAME 3</div>

  <!-- Frame 4 -->
  <section class="frame f4">
    <svg class="icon" style="left:67px;top:9px" width="26" height="26" viewBox="0 0 26 26" aria-hidden="true">
      <polygon points="7,2 19,2 25,13 19,24 7,24 1,13" fill="none" stroke="var(--yellow)" stroke-width="2"/>
      <circle cx="13" cy="13" r="4" fill="var(--yellow)"/>
    </svg>
    <div class="abs center-x codes" style="top:37px">KRV / ZLT / NOX / VELCON /<br>DRAM / etc...</div>
    <svg class="icon" style="left:67px;top:69px" width="26" height="26" viewBox="0 0 26 26" aria-hidden="true">
      <polygon points="7,2 19,2 25,13 19,24 7,24 1,13" fill="none" stroke="var(--lime)" stroke-width="2"/>
      <text x="13" y="17.5" font-size="13" font-weight="700" text-anchor="middle" fill="var(--lime)">$</text>
    </svg>
    <div class="abs center-x codes" style="top:97px">EURO / USD / TLY /<br>CHF / etc...</div>
  </section>
  <div class="frame-label f4">FRAME 4</div>

  <!-- Frame 5 -->
  <section class="frame f5">
    <div class="abs center-x pay-title" style="top:17px">Payment Options</div>
    <div class="pay-box" style="left:28px;top:42px">Vorn</div>
    <div class="pay-box" style="left:83px;top:42px">Glimra</div>
    <div class="pay-box" style="left:28px;top:68px">Trovan</div>
    <div class="pay-box" style="left:83px;top:68px">Zelbix</div>
    <div class="pay-box pay-card" style="left:45px;top:94px">Kestra</div>
    <div class="pay-box pay-card" style="left:81px;top:94px">Orvane</div>
  </section>
  <div class="frame-label f5">FRAME 5</div>

  <!-- Frame 6 -->
  <section class="frame f6">
    <div class="abs center-x pay-title" style="top:13px">All in One Plattform</div>
    <svg class="icon" style="left:33px;top:38px" width="24" height="25" viewBox="0 0 24 25" aria-hidden="true">
      <polygon points="12,1 23,7 23,18 12,24 1,18 1,7" fill="var(--hex-blue)"/>
      <path d="M6 16 L10 11 L13 14 L18 8" fill="none" stroke="#fff" stroke-width="1.6"/>
    </svg>
    <svg class="icon" style="left:93px;top:38px" width="24" height="25" viewBox="0 0 24 25" aria-hidden="true">
      <polygon points="12,1 23,7 23,18 12,24 1,18 1,7" fill="var(--hex-green)"/>
      <path d="M7 17 L11 13 M10 9 L15 14 M12 8 L16 12 M13 8 L17 4 M16 12 L20 8" stroke="#fff" stroke-width="1.8" stroke-linecap="round"/>
    </svg>
    <div class="abs hub-label" style="left:15px;width:60px;text-align:center;top:67px">Exchange</div>
    <div class="abs hub-label" style="left:75px;width:60px;text-align:center;top:67px">Mining</div>
    <svg class="icon" style="left:33px;top:85px" width="24" height="25" viewBox="0 0 24 25" aria-hidden="true">
      <polygon points="12,1 23,7 23,18 12,24 1,18 1,7" fill="var(--hex-purple)"/>
      <rect x="6" y="7" width="12" height="11" fill="none" stroke="#fff" stroke-width="1.5"/>
      <path d="M10 7 V18 M14 7 V18" stroke="#fff" stroke-width="1.5"/>
    </svg>
    <svg class="icon" style="left:93px;top:85px" width="24" height="25" viewBox="0 0 24 25" aria-hidden="true">
      <polygon points="12,1 23,7 23,18 12,24 1,18 1,7" fill="var(--hex-red)"/>
      <path d="M5 8 H8 L10 15 H17 L18 10 H9" fill="none" stroke="#fff" stroke-width="1.6"/>
      <circle cx="11" cy="18" r="1.2" fill="#fff"/><circle cx="16" cy="18" r="1.2" fill="#fff"/>
    </svg>
    <div class="abs hub-label" style="left:15px;width:60px;text-align:center;top:114px">ATMs</div>
    <div class="abs hub-label" style="left:65px;width:80px;text-align:center;top:114px">Payment Solution</div>
  </section>
  <div class="frame-label f6">FRAME 6</div>

</body>
</html>
```